Brochure Design Project for Home Watch company

We are a new start up company in fast growing home watch industry. We provide services in Hawaii so the design needs to be reflect that. Our web site can give you overview of what we do - www.breezekeepcare.com. We will service clients that own second homes in Hawaii. These properties are not necessarily income producing properties for our clients. I'm looking for 2 or 4 page brochure which will be used to market our services to potential new clients. It needs to be high quality, modern with slight Hawaiian feel (we are based on Oahu). I'm not looking for a trifold type of brochure.

We are open to various colors based on what the designer might suggest but as you can see on our home page - the main picture of the home on our site has lots of red and white which we like as well as the "head" or dot above the "i" in our logo is red. I was not able to upload the file of the main house (purchased on snapmeadow) on here therefore I'll have to provide the original photo to the selected designer at the later time. For now I just uploaded the not purchased copy.

If you have other questions please do let me know. And lastly, I will be looking to create a business card and post card as well.

```html
<!DOCTYPE html>
<html lang="en">
<head>
<meta charset="utf-8">
<title>Breeze Keep Care – Brochure</title>
<link href="https://fonts.googleapis.com/css2?family=Montserrat:wght@300;400;500;600;700&display=swap" rel="stylesheet">
<style>
:root{
  --red:#e65a5c;
  --red-dark:#d9484b;
  --ink:#3a3a3a;
  --muted:#6b6b6b;
  --paper:#ffffff;
  --bg:#e4e4e4;
}
*{box-sizing:border-box;margin:0;padding:0}
html,body{width:960px;height:1200px;overflow:hidden}
body{background:var(--bg);font-family:"Montserrat",sans-serif;color:var(--ink);position:relative}
.spread{position:absolute;left:40px;width:880px;height:540px;display:flex;box-shadow:0 12px 30px rgba(0,0,0,.18)}
.spread--outer{top:40px}
.spread--inner{top:620px}
.page{position:relative;width:440px;height:540px;background:var(--paper);overflow:hidden}
.page--left{background:linear-gradient(90deg,#fff 85%,#f1f1f1)}
.photo{position:absolute;display:block}
.shape{position:absolute;left:0;top:0}

/* back page */
.family-photo{left:0;top:0;width:440px;height:165px;background:linear-gradient(180deg,#c9b8a3,#a88f76 60%,#8a7c6d)}
.about{position:absolute;left:30px;top:180px;width:390px}
.about h2{font-weight:400;color:var(--red);font-size:19px;line-height:1.2;margin-bottom:10px}
.about p{font-size:8.6px;font-weight:300;line-height:1.5;margin-bottom:7px}
.badge{position:absolute;left:30px;top:398px;width:150px}
.badge__mark{width:120px;height:30px;border-radius:4px;background:#dfe4ef;margin-bottom:8px}
.badge p{font-size:8.4px;font-weight:300;line-height:1.45}
.contact{position:absolute;right:0;top:400px;width:240px;height:120px;background:var(--red);color:#fff;padding:12px 18px 0 22px}
.contact li{list-style:none;display:flex;gap:8px;align-items:flex-start;font-size:9.6px;font-weight:300;line-height:1.35;margin-bottom:8px}
.contact svg{flex:none;margin-top:1px}

/* cover */
.brand{position:absolute;left:32px;top:28px;display:flex;align-items:center;gap:8px}
.brand__dot{width:12px;height:12px;border-radius:50%;background:var(--red)}
.brand__name{font-weight:600;font-size:14px;color:var(--ink)}
.villa-photo{left:0;top:80px;width:440px;height:300px;background:linear-gradient(180deg,#8cc2e6 0%,#c8dbe6 30%,#b7a999 48%,#2a6f94 62%,#1c5476)}
.cover-title{position:absolute;left:36px;top:392px;color:#fff;font-weight:300;font-size:19px;line-height:1.25}
.cover-url{position:absolute;left:36px;bottom:20px;font-size:10px;font-weight:400;color:var(--muted);letter-spacing:.3px}

/* inner left */
.intro{position:absolute;left:30px;top:28px;width:380px}
.intro h2{color:var(--red);font-weight:400;font-size:20px;margin-bottom:8px}
.intro p{font-size:8.6px;font-weight:300;line-height:1.5}
.house-illustration{left:70px;top:95px;width:290px;height:160px;background:linear-gradient(180deg,#f2f2f2,#d8d8d8);border-radius:6px}
.service{position:absolute}
.service h3{color:var(--red);font-weight:600;font-size:10.4px;line-height:1.25;margin-bottom:5px}
.service p{font-size:8.5px;font-weight:300;line-height:1.5}
.service--outdoor{left:30px;top:290px;width:170px}
.service--exterior{left:230px;top:270px;width:180px}
.service--interior{left:30px;top:410px;width:380px}
.bottom-bar{position:absolute;left:0;right:0;bottom:0;height:7px;background:var(--red)}

/* inner right */
.aerial-photo{left:0;top:0;width:440px;height:160px;background:linear-gradient(135deg,#6e7b6a,#4f6b5c 45%,#1d6d78 70%,#2a8fa0)}
.aerial-caption{position:absolute;left:22px;top:112px;width:380px;color:#fff;font-size:9px;font-weight:300;line-height:1.45}
.concierge{position:absolute}
.concierge small{display:block;font-size:7.5px;color:var(--muted);font-weight:300;margin-bottom:2px}
.concierge h3{color:var(--red);font-weight:600;font-size:13px;margin-bottom:5px}
.concierge p{font-size:8.3px;font-weight:300;line-height:1.5}
.concierge--pre{left:24px;top:180px;width:185px}
.concierge--post{left:230px;top:180px;width:185px}
.concierge--special{left:24px;top:360px;width:392px}
</style>
</head>
<body>

<section class="spread spread--outer">
  <article class="page page--left back-page">
    <div class="photo family-photo" role="img" aria-label="Photo of the owning family smiling together on a beach"></div>
    <div class="about">
      <h2>We are a family run and<br>operated business.</h2>
      <p>Leilani is licensed real estate broker in Hawaii. She has 10+ years' work experience at a major global commercial real estate company. She loves to work with people, find solutions to specific problems, and add value to everything she does.</p>
      <p>Kai owns a handyman and landscaping firm that is based on two simple principles: Pay extra attention to details, and under promise and over deliver. And all of his clients would attest that his firm's attention to detail and his perfectionism, as well as his ethical and professional approach are practically unmatched.</p>
    </div>
    <div class="badge">
      <div class="badge__mark" role="img" aria-label="Accredited member badge"></div>
      <p>We are Accredited Members of the HCGA. We are insured and bonded, and we agreed to uphold the strictest and most ethical standards in the industry</p>
    </div>
    <svg class="shape" width="440" height="540" viewBox="0 0 440 540"><polygon points="200,402 440,378 440,404 200,404" fill="var(--red)"/></svg>
    <ul class="contact">
      <li><svg width="10" height="12" viewBox="0 0 10 12"><path d="M5 0a4 4 0 0 1 4 4c0 3-4 8-4 8S1 7 1 4a4 4 0 0 1 4-4z" fill="none" stroke="#fff"/><circle cx="5" cy="4" r="1.3" fill="#fff"/></svg><span>Breeze Keep Care LLC<br>Honolulu Hawaii</span></li>
      <li><svg width="11" height="11" viewBox="0 0 11 11"><circle cx="5.5" cy="5.5" r="5" fill="none" stroke="#fff"/><path d="M3.5 3.2l1.2 0 .5 1.4-.7.6a4 4 0 0 0 1.8 1.8l.6-.7 1.4.5v1.2c-3 .3-5.3-2-4.8-4.8z" fill="#fff"/></svg><span>808-555-0142</span></li>
      <li><svg width="11" height="9" viewBox="0 0 11 9"><rect x=".5" y=".5" width="10" height="8" fill="none" stroke="#fff"/><path d="M.5.5l5 4 5-4" fill="none" stroke="#fff"/></svg><span>hello@breezekeepcare.com</span></li>
      <li><svg width="11" height="11" viewBox="0 0 11 11"><circle cx="5.5" cy="5.5" r="5" fill="none" stroke="#fff"/><ellipse cx="5.5" cy="5.5" rx="2.2" ry="5" fill="none" stroke="#fff"/><path d="M.5 5.5h10" stroke="#fff"/></svg><span>www.breezekeepcare.com</span></li>
    </ul>
  </article>

  <article class="page cover-page">
    <div class="brand"><span class="brand__dot"></span><span class="brand__name">Breeze Keep Care</span></div>
    <div class="photo villa-photo" role="img" aria-label="Photo of a modern white Hawaiian villa with an infinity pool overlooking the ocean"></div>
    <svg class="shape" width="440" height="540" viewBox="0 0 440 540"><polygon points="0,378 440,300 440,490 0,490" fill="var(--red)"/></svg>
    <h1 class="cover-title">Providing Premiere<br>Home Watch and<br>Concierge Services</h1>
    <p class="cover-url">www.breezekeepcare.com</p>
  </article>
</section>

<section class="spread spread--inner">
  <article class="page page--left">
    <div class="intro">
      <h2>What do we do?</h2>
      <p>We save your time. We perform visual inspections and provide our presence while you are away so you can enjoy your time and home while you are on the island. We have your back!</p>
    </div>
    <div class="photo house-illustration" role="img" aria-label="Illustration of a house cross-section with icons for each inspection point"></div>
    <div class="service service--outdoor">
      <h3>General Outdoor Visual<br>Inspections</h3>
      <p>Check yard, lawn and landscaping; check lanai, deck, and pool area for any damage; check for mold or fading of all outdoor furniture; check water level of swimming pool or hot tub, if applicable</p>
    </div>
    <div class="service service--exterior">
      <h3>Home Exterior Visual<br>Inspections</h3>
      <p>Check security cameras; check for overall damage; remove mail, newspapers, and flyers from mailbox and store inside of the property; check outdoor plumbing and hoses for leakage; check garage; check for vandalism and theft</p>
    </div>
    <div class="service service--interior">
      <h3>Home Interior Visual Inspections</h3>
      <p>Make sure security system is in working order; ensure that all doors, windows and sliders are locked and secured; check thermostats and make sure the air conditioning is set at appropriate and requested temperature; make sure all smoke detectors are in proper working order or replace batteries if necessary; visually inspect the water heater and washer and dryer</p>
    </div>
    <div class="bottom-bar"></div>
  </article>

  <article class="page">
    <div class="photo aerial-photo" role="img" aria-label="Aerial photo of an Oahu coastline neighbourhood and reef"></div>
    <p class="aerial-caption">Don't let repairs or unexpected surprises upon your arrival take away from your vacation time. Arrive knowing all you need to do in Hawaii is relax and enjoy your second home and the island.</p>
    <div class="concierge concierge--pre">
      <small>Concierge Services</small>
      <h3>Pre-Arrival</h3>
      <p>Groceries purchased and stored, air conditioning and ceiling vents turned on and/or windows opened, water turned on, flowers placed, fresh laundered linens on beds, towels arranged in the bathrooms, deck furniture placed on decks and patio, house freshened up and aired out, security system disarmed as appropriate, decks, walkways, lanais and driveways cleaned of debris and special requests completed.</p>
    </div>
    <div class="concierge concierge--post">
      <small>Concierge Services</small>
      <h3>Post-Departure</h3>
      <p>House cleaning coordinated, beds made, sheets and towels cleaned, dishes washed and put away, all doors and windows secured, lights on timers set, water turned off, outdoor furniture stored or covered per specific instructions, driveways, lanais, walkways and decks cleared of debris, air conditioning set for appropriate level, trash placed for collection and security system turned on.</p>
    </div>
    <div class="concierge concierge--special">
      <small>Concierge Services</small>
      <h3>Sample of Special Services/Requests</h3>
      <p>Key holding services, mail forwarding, coordination of transportation from and to the airport, light handyman and landscaping services, vendor coordination (we coordinate access and meet everyone you authorize at your home including but not limited to maintenance, repair, pest control, landscaping and tree trimming, and utility providers), pre-storm services (secure outdoor furniture, potted plants, hammocks and any other outdoor items, etc.) and post-storm services (clean walkway and driveway, pick-up trash, etc.), and emergency services response, etc. Additional services and pricing available upon request.</p>
    </div>
    <div class="bottom-bar"></div>
  </article>
</section>

</body>
</html>
```